Stationary and document suite for consultancy business in Australia called Calverdo

I would like to get a suite of documents suitable for my new business called Calverdo. I have included the original brief below, however have already selected a design for the logo. I would like to get:
Letter head - simple letter template with "V" logo embossed in background
Word document - standard format with "V" logo embossed in background
Proposal document - bolder pages with cover and back cover, include empty pages with footer as well as contents
Powerpoint presentation - open to ideas
Email signature - banner style or text, open to ideas
Brief that was given for logo (logo not required)
The name of the business is derived from the latin word for green ("Viridis") combined with "co" which is intended to represent a number of different words: collaborative, cooperative, coaching, collective,  construction, consulting, etc.
My objective for the brand is to represent a dynamic, progressive and collaborative business, where our people have fun and enjoy their work.
The objective of our business is to provide consultancy services to construction businesses, mainly aimed at building high performing teams and strategic growth. We will create learning and development tools that businesses can use to increase staff satisfaction and retention. Our future goal is to invest in decarbonisation and sustainability technology for use in the construction industry.
Our target market is construction business leaders and infrastructure owners, who operate road, rail and utility assets. We also want to present as a dynamic, progressive and fun place to work that will be attractive to new employees.

```html
<!DOCTYPE html>
<html lang="en">
<head>
<meta charset="utf-8">
<title>Calverdo Presentation Suite</title>
<link href="https://fonts.googleapis.com/css2?family=Roboto:ital,wght@0,300;0,400;0,500;0,700;1,400&display=swap" rel="stylesheet">
<style>
:root{
  --green:#8cc63f;
  --charcoal:#48484a;
  --ink:#333333;
  --grey:#6f6f71;
  --rule:#222222;
  --page:#ffffff;
  --backdrop:#d4d4d4;
}
*{box-sizing:border-box;margin:0;padding:0}
html,body{width:1200px;height:942px;overflow:hidden}
body{background:var(--backdrop);font-family:"Roboto",Arial,sans-serif;color:var(--ink);position:relative}
.slide{position:absolute;width:362px;height:271px;background:var(--page);box-shadow:0 1px 3px rgba(0,0,0,.25);overflow:hidden}
.col-1{left:29px}.col-2{left:414px}.col-3{left:800px}
.row-1{top:21px}.row-2{top:327px}.row-3{top:632px}
.slide--dark{background:var(--charcoal)}
.slide--light{background:linear-gradient(#ffffff,#d9d7d6)}
.abs{position:absolute}

/* cover */
.cover-brand{position:absolute;right:36px;top:142px;font-size:30px;font-weight:300;letter-spacing:1px}
.slide--dark .cover-brand{color:#fff}
.slide--light .cover-brand{color:var(--grey)}
.cover-title{position:absolute;right:36px;top:192px;text-align:right;line-height:1}
.cover-title .welcome{color:var(--green);font-weight:700;font-size:16.5px}
.cover-title .name{font-weight:500;font-size:16px;margin-top:1px}
.slide--dark .cover-title .name{color:#fff}
.slide--light .cover-title .name{color:var(--grey)}
.cover-title .desc{color:var(--green);font-style:italic;font-size:12.5px;margin-top:1px}

/* page header / footer */
.page-title{position:absolute;left:19px;top:22px;color:var(--green);font-weight:700;font-size:17px;letter-spacing:.3px}
.page-sub{position:absolute;left:19px;top:40px;font-size:9.5px;color:var(--ink)}
.page-rule{position:absolute;left:79px;top:45px;width:200px;height:1px;background:var(--rule)}
.page-brand{position:absolute;right:19px;top:37px;font-size:12px;font-weight:400;color:var(--grey)}
.page-foot-rule{position:absolute;left:19px;right:19px;top:240px;height:1.5px;background:var(--green)}
.page-url{position:absolute;left:19px;top:245px;font-size:7.5px;color:var(--ink)}
.page-url b{font-weight:700}
.page-num{position:absolute;right:19px;top:246px;font-size:6.5px;color:var(--ink)}

/* contents */
.toc{position:absolute;left:29px;right:30px;top:64px;list-style:none}
.toc li{display:flex;align-items:center;height:30.3px;font-size:9.5px;color:var(--ink)}
.toc .dots{flex:1;border-bottom:1px dotted #aaa;margin:5px 4px 0}
.toc .pg{font-size:6px;margin-top:5px}

/* about */
.member{position:absolute;top:66px;width:72px}
.photo{width:72px;height:72px;background:var(--charcoal);border:2px solid #fff;box-shadow:0 0 2px rgba(0,0,0,.4);display:flex;align-items:center;justify-content:center;color:#bbb;font-size:9px}
.member-name{color:var(--green);font-size:7px;margin-top:9px}
.member-role{font-size:4.6px;line-height:1.2;margin-top:1px}
.member-bio{font-size:4.8px;line-height:1.4;margin-top:14px;text-align:justify}
.divider{position:absolute;top:66px;width:1px;height:147px;background:#555}

/* bullets */
.bullets{position:absolute;left:22px;right:26px;top:74px;list-style:none}
.bullets li{position:relative;padding-left:13px;font-size:5.7px;line-height:1.5;margin-bottom:8.5px;text-align:justify}
.bullets li::before{content:"";position:absolute;left:1px;top:2px;width:3.5px;height:3.5px;border-radius:50%;background:var(--green)}

/* chart */
.note{font-size:5px;line-height:1.6;color:var(--ink)}

/* services */
.services{position:absolute;left:38px;right:40px;top:66px;list-style:none}
.services li{font-size:5.3px;line-height:1.6;margin-bottom:7.5px;text-align:justify}

/* back cover */
.thanks{position:absolute;right:38px;top:143px;text-align:right;line-height:1}
.thanks .big{color:var(--green);font-size:40px;font-weight:300}
.thanks .small{color:#fff;font-size:22px;font-weight:300}
.contact{position:absolute;right:40px;top:220px;text-align:right;color:#fff;font-size:7px;line-height:1.3}
.contact span{display:flex;justify-content:flex-end;align-items:center;gap:4px}
.contact i{display:inline-block;width:5px;height:5px;background:var(--green);border-radius:50%}
</style>
</head>
<body>

<section class="slide slide--dark col-1 row-1">
  <div class="cover-brand">Calverdo</div>
  <div class="cover-title">
    <div class="welcome">Welcome to Our</div>
    <div class="name">PRESENTATION NAME</div>
    <div class="desc">Description</div>
  </div>
</section>

<section class="slide slide--light col-2 row-1">
  <div class="cover-brand">Calverdo</div>
  <div class="cover-title">
    <div class="welcome">Welcome to Our</div>
    <div class="name">PRESENTATION NAME</div>
    <div class="desc">Description</div>
  </div>
</section>

<section class="slide col-3 row-1">
  <div class="page-title">CONTENTS</div>
  <div class="page-sub">Sub Heading</div>
  <div class="page-rule"></div>
  <div class="page-brand">Calverdo</div>
  <ul class="toc">
    <li>I&nbsp; ABOUT US<span class="dots"></span><span class="pg">2</span></li>
    <li>II&nbsp; OUR SERVICES<span class="dots"></span><span class="pg">3</span></li>
    <li>III&nbsp; CASE STUDY<span class="dots"></span><span class="pg">4</span></li>
    <li>IV&nbsp; DIAGRAM<span class="dots"></span><span class="pg">5</span></li>
    <li>V&nbsp; CONTACUS<span class="dots"></span><span class="pg">6</span></li>
  </ul>
  <div class="page-foot-rule"></div>
  <div class="page-url">www.<b>calverdo</b>.com.au</div>
  <div class="page-num">PAGE1</div>
</section>

<section class="slide col-1 row-2">
  <div class="page-title">ABOUT US</div>
  <div class="page-sub">Sub Heading</div>
  <div class="page-rule"></div>
  <div class="page-brand">Calverdo</div>
  <div class="member" style="left:33px">
    <div class="photo" role="img" aria-label="Team member portrait">Photo</div>
    <div class="member-name">Mr Nobody</div>
    <div class="member-role">Team lead and senior coach</div>
    <div class="member-bio">Helps builders grow strong teams through clear goals, honest talk and steady weekly coaching on site.</div>
  </div>
  <div class="divider" style="left:120px"></div>
  <div class="member" style="left:139px">
    <div class="photo" role="img" aria-label="Team member portrait">Photo</div>
    <div class="member-name">Mr Nobody</div>
    <div class="member-role">Strategy and growth lead</div>
    <div class="member-bio">Works with owners on growth plans, hiring and the steps that keep good people in the business.</div>
  </div>
  <div class="divider" style="left:231px"></div>
  <div class="member" style="left:248px">
    <div class="photo" role="img" aria-label="Team member portrait">Photo</div>
    <div class="member-name">Mr Nobody</div>
    <div class="member-role">Learning tools designer</div>
    <div class="member-bio">Builds training tools that crews enjoy using and that lift staff satisfaction over time.</div>
  </div>
  <div class="page-foot-rule"></div>
  <div class="page-url">www.<b>calverdo</b>.com.au</div>
  <div class="page-num">PAGE1</div>
</section>

<section class="slide col-2 row-2">
  <div class="page-title">BULLET TEXT</div>
  <div class="page-sub">Sub Heading</div>
  <div class="page-rule"></div>
  <div class="page-brand">Calverdo</div>
  <ul class="bullets">
    <li>We help construction leaders build high performing teams that stay, grow and deliver safe, steady work on every project they take on.</li>
    <li>Our coaching links daily site work with long term goals, so managers can see progress and people know where they stand.</li>
    <li>We design learning tools that fit busy crews, short and practical, and that lift satisfaction and retention across the business.</li>
    <li>Strategy sessions help owners plan for growth, choose the right projects and build the team they need to win them with confidence over the coming years.</li>
    <li>Looking ahead, we will invest in decarbonisation and sustainability tools for road, rail and utility owners across Australia.</li>
  </ul>
  <div class="page-foot-rule"></div>
  <div class="page-url">www.<b>calverdo</b>.com.au</div>
  <div class="page-num">PAGE1</div>
</section>

<section class="slide col-3 row-2">
  <div class="page-title">CASE STUDY</div>
  <div class="page-sub">Sub Heading</div>
  <div class="page-rule"></div>
  <div class="page-brand">Calverdo</div>
  <svg class="abs" style="left:38px;top:66px" width="146" height="112" viewBox="0 0 146 112" font-family="Roboto, sans-serif">
    <g stroke="#cfcfcf" stroke-width=".6">
      <line x1="0" y1="2" x2="144" y2="2"/><line x1="0" y1="12" x2="144" y2="12"/>
      <line x1="0" y1="22" x2="144" y2="22"/><line x1="0" y1="32" x2="144" y2="32"/>
      <line x1="0" y1="42" x2="144" y2="42"/><line x1="0" y1="52" x2="144" y2="52"/>
      <line x1="0" y1="62" x2="144" y2="62"/><line x1="0" y1="72" x2="144" y2="72"/>
      <line x1="0" y1="82" x2="144" y2="82"/><line x1="0" y1="92" x2="144" y2="92"/>
      <line x1="0" y1="102" x2="144" y2="102"/>
    </g>
    <g fill="#8cc63f">
      <rect x="33" y="6" width="17" height="102"/>
      <rect x="52" y="20" width="17" height="88"/>
      <rect x="72" y="45" width="17" height="63"/>
      <rect x="91" y="28" width="17" height="80"/>
    </g>
    <g fill="#fff" font-size="5.5">
      <text transform="translate(44 105) rotate(-90)">Sub text1</text>
      <text transform="translate(63 105) rotate(-90)">Sub text2</text>
      <text transform="translate(83 105) rotate(-90)">Sub text3</text>
      <text transform="translate(102 105) rotate(-90)">Sub text4</text>
    </g>
  </svg>
  <p class="note abs" style="left:218px;top:70px;width:100px">Road upgrade program for a regional owner. Team retention rose within one year of coaching, and two site leads were promoted from inside the crew.</p>
  <p class="note abs" style="left:217px;top:124px;width:100px">Leaders met weekly, staff surveys improved, and the project was delivered on time and on budget with no lost time injuries.</p>
  <p class="note abs" style="left:34px;top:196px;width:294px;text-align:justify">A six month coaching program helped a rail maintenance crew lift engagement, cut turnover and plan for growth. Results were shared with the client board and used to shape the next phase of work, which now covers three more regional depots and a new graduate intake.</p>
  <div class="page-foot-rule"></div>
  <div class="page-url">www.<b>calverdo</b>.com.au</div>
  <div class="page-num">PAGE1</div>
</section>

<section class="slide col-1 row-3">
  <div class="page-title">DIAGRAM</div>
  <div class="page-sub">Sub Heading</div>
  <div class="page-rule"></div>
  <div class="page-brand">Calverdo</div>
  <p class="note abs" style="left:30px;top:78px;width:150px;text-align:right;font-size:5.4px">Our work splits across team coaching, strategy and learning tools. Each stream supports the people who build and run roads, rail and utility assets across Australia. We focus on growth, staff retention and safe delivery, and we measure each program against clear goals agreed with the client at the start. Leaders get short reports each month, and crews see their own progress in simple charts they can share.</p>
  <p class="note abs" style="left:30px;top:182px;width:150px;text-align:right;font-size:5.4px">Future work will add decarbonisation and sustainability tools for the construction sector, built with partners and tested on live projects before release.</p>
  <svg class="abs" style="left:230px;top:68px" width="82" height="82" viewBox="-41 -41 82 82">
    <g stroke="#fff" stroke-width=".8" transform="rotate(-8)">
      <path d="M0 0 L0 -40 A40 40 0 0 1 28 -28.5 Z" fill="#6f6f71"/>
      <path d="M0 0 L28 -28.5 A40 40 0 0 1 40 3 Z" fill="#8cc63f"/>
      <path d="M0 0 L40 3 A40 40 0 0 1 16 37 Z" fill="#6f6f71"/>
      <path d="M0 0 L16 37 A40 40 0 1 1 0 -40 Z" fill="#8cc63f"/>
    </g>
  </svg>
  <div class="abs note" style="left:228px;top:164px;width:100px;font-size:4.8px">
    <div style="display:flex;align-items:center;gap:5px;border-bottom:.6px solid #999;padding-bottom:2px"><i style="width:6px;height:6px;background:var(--green)"></i>Team coaching 50%</div>
    <div style="display:flex;align-items:center;gap:5px;border-bottom:.6px solid #999;padding:3px 0 2px"><i style="width:6px;height:6px;background:var(--grey)"></i>Strategy work 50%</div>
  </div>
  <p class="note abs" style="left:228px;top:194px;width:106px;font-size:4.6px">Figures show share of hours billed in the last financial year.</p>
  <div class="page-foot-rule"></div>
  <div class="page-url">www.<b>calverdo</b>.com.au</div>
  <div class="page-num">PAGE1</div>
</section>

<section class="slide col-2 row-3">
  <div class="page-title">OUR SERVICES</div>
  <div class="page-sub">Sub Heading</div>
  <div class="page-rule"></div>
  <div class="page-brand">Calverdo</div>
  <ol class="services">
    <li>1. Team coaching for site and project leaders.</li>
    <li>2. Strategic growth plans for construction businesses that want to take on larger work.</li>
    <li>3. Learning and development tools that lift staff satisfaction, built to suit busy crews and short breaks on site.</li>
    <li>4. Retention reviews with clear actions for managers, covering pay, workload, career paths and the way teams are led day to day.</li>
    <li>5. Workshops that help crews collaborate, plan and solve problems together on live projects. Each session is shaped around the client's own sites, people and goals, and ends with a short list of actions the team owns and tracks.</li>
    <li>6. Sustainability advice for road, rail and utility owners who want to cut carbon across their assets, from early planning through to delivery, with practical steps that fit existing budgets and the way their teams already work.</li>
  </ol>
  <div class="page-foot-rule"></div>
  <div class="page-url">www.<b>calverdo</b>.com.au</div>
  <div class="page-num">PAGE1</div>
</section>

<section class="slide slide--dark col-3 row-3">
  <div class="thanks">
    <div class="big">Thanks</div>
    <div class="small">For Coming</div>
  </div>
  <div class="contact">
    <span>+61 400 000 123 <i></i></span>
    <span>hello@calverdo.com.au <i></i></span>
    <span>calverdo.com.au <i></i></span>
  </div>
</section>

</body>
</html>
```